Wordpress Theme for Larchwell Clinic

** Please view updated Sitemap2.pdf doc to clarify some confusion ***

This is a multiuser WordPress subscription site for Larchwell Clinic. Please see attachment for sitemap. Please do not include extra content like social media icons, search bars, or images. If you have questions, please ask for clarification.
The site contains the following pages and sub-pages:

1. Home
2. Our Clinic
2a. Our Clinic > Mission
2b. Our Clinic > Services
2c. Our Clinic > Clinic Policies
2d. Our Clinic > Schedules
3. Our Staff
3a. Our Staff > [Staff member page]
4. Resources
4a. Resources > Patient Health (index)
4b. Resources > Patient Health (index) > [post]
4c. Resources > Links
4d. Resources > Forms
5. Alerts
5a. Alerts > [Alert Page]
6. Contact Us

Includes the Following Pages, Subpages, and Content
1. Home
a. About Us
b. Our Staff
c. Bulletins
d. Accepting New Patients (shown as an alert widget)
e. Links
i. Physician Toolbox
ii. Book an Appointment
f. Clinic Policies
i. Show first 3 policies (e.g. Late Arrivals, Missed Appointments, Fees)
ii. Link to Clinic Policies page
g. Primary widget (displayed on all pages)
i. Hours of operation
ii. Contact Info
1. Tel
2. Fax
3. Email
4. Address
5. Get directions (link to Google Maps)
2. Our Clinic
a. Main Page
i. Clinic Name
ii. Overview
iii. Languages Spoken
iv. Secondary Navigation
1. Mission
2. Services
3. Clinic Policies
4. Schedules (see attachment)
b. Our Clinic > Mission
c. Our Clinic > Services
i. For each service include service TITLE and DESCRIPTION
d. Our Clinic > Clinic Policies
i. For each policy include policy TITLE and DESCRIPTION
ii. Include the following policies in mockup
1. Late arrivals
2. Missed appointments
3. Fees for missed appointments
4. Referrals and follow-ups
5. Services not covered by RDV
6. Information for TQL patients
7. Medical Legal Reports
e. Our Clinic > Schedules
3. Our Staff
a. Main Page
i. Display a list of staff members. Include NAME and DESIGNATION
b. Our Staff > [Staff Name]
i. Include NAME, PICTURE, DESIGNATION, and BIO
4. Resources
a. Resources > Patient Health
i. Main Page
1. Posts (ordered by date)
a. Title
b. Summary
2. Side Navigation
a. Post Categories
ii. Patient Health > [post title]
1. Title
2. Post Category
3. Date
4. Author
5. Summary
6. Body
b. Resources > Links
1. Secondary Navigation - Categories
a. Sample Categories:
i. Local Services
ii. RDV and Drug Coverage
iii. Mental Health Resources
2. Category page
a. Include the following links in the 'Local Services' category
i. Hypertension clinics
ii. Home Care services
iii. Vaccine Clinics
c. Resources > Forms
i. Display a table with form TITLE and CATEGORY
ii. Side Navigation
1. Form Categories
a. Use the following sample Categories
i. Referrals
ii. Insurance
iii. Intake
iv. Discharge
v. Waivers
5. Alerts
a. Main page
i. List of all Alert posts
1. Include post TITLE as a link to the post
ii. Side Navigation
1. Alerts Archive
a. shown as Month + Number of posts
iii. Alerts > [Alert page]
1. Include TITLE, DATE, AUTHOR, BODY
6. Contact Us
a. Map
b. Hours of operation
c. Address
d. Phone number
e. Fax number
e. Fax number
f. Map
g. Email

Design notes:
- fixed width
- responsive (need designs for mobile, tablet, and desktop)
- simple, dark font, white background
- use Font Awesome icons where needed
- user adds own logo

Target Market(s)

Larchwell Clinic

Industry/Entity Type

Medical

Number of Pages Required

5+ page

Font styles to use
Serif
Sans Serif

Requirements
Must have
• Please keep designs very simple.
• Examples:
• https://www.quandrix.com/install
• http://www.tervolane.com/company/about-us
• http://brightnumberhub.org/
• http://www.vorn.com/
Should not have
• Minimal or no use of shadows and gradients

```html
<!DOCTYPE html>
<html lang="en">
<head>
<meta charset="utf-8">
<title>Larchwell Clinic – Resources Links</title>
<link rel="stylesheet" href="https://fonts.googleapis.com/css2?family=Open+Sans:wght@400;600;700&display=swap">
<style>
  :root {
    --brand-blue: #0b8de0;
    --text-dark: #2b2b2b;
    --text-body: #333333;
    --band-grey: #f7f7f7;
    --rule-grey: #dddddd;
    --footer-bg: #262626;
    --footer-muted: #8a8a8a;
    --footer-heading: #a0a0a0;
    --footer-rule: #555555;
    --white: #ffffff;
  }
  * { margin: 0; padding: 0; box-sizing: border-box; }
  html, body { width: 1200px; height: 748px; overflow: hidden; background: var(--white); }
  body { position: relative; font-family: "Open Sans", Arial, sans-serif; color: var(--text-body); }
  a { color: inherit; text-decoration: none; }
  ul { list-style: none; }

  .top-bar { position: absolute; left: 0; top: 0; width: 1200px; height: 30px; background: var(--brand-blue); color: var(--white); font-size: 9.5px; }
  .top-bar .contact-line { position: absolute; left: 162px; top: 9px; }
  .top-bar .quick-links { position: absolute; right: 161px; top: 9px; }
  .top-bar .sep { display: inline-block; width: 1px; height: 14px; background: var(--white); vertical-align: -3px; margin: 0 5px 0 5px; }

  .site-header { position: absolute; left: 0; top: 30px; width: 1200px; height: 83px; }
  .brand { position: absolute; left: 162px; top: 27px; display: flex; align-items: center; gap: 12px; font-size: 21px; font-weight: 600; color: var(--text-dark); }
  .brand-mark { width: 24px; height: 24px; border-radius: 50%; background: var(--brand-blue); }
  .main-nav a { position: absolute; top: 0; height: 83px; line-height: 83px; font-size: 10.5px; color: var(--text-dark); }
  .main-nav a.active { background: var(--brand-blue); color: var(--white); width: 60px; text-align: center; }

  .page-title-band { position: absolute; left: 0; top: 113px; width: 1200px; height: 59px; background: var(--band-grey); color: var(--text-dark); }
  .page-title-band h1 { position: absolute; left: 162px; top: 15px; font-size: 10px; font-weight: 700; }
  .page-title-band .breadcrumb { position: absolute; left: 162px; top: 34px; font-size: 9.5px; }

  .section-heading { position: absolute; top: 217px; font-weight: 700; color: var(--text-dark); border-bottom: 1px solid var(--rule-grey); padding-bottom: 5px; }
  .side-nav-heading { left: 162px; width: 202px; font-size: 10px; top: 219px; padding-bottom: 5px; }
  .content-heading { left: 387px; width: 651px; font-size: 12.5px; }

  .side-nav { position: absolute; left: 162px; top: 257px; border-left: 3px solid var(--rule-grey); padding-left: 11px; font-size: 9.5px; }
  .side-nav li { height: 22.5px; line-height: 16px; color: var(--text-dark); }
  .side-nav li.current { color: var(--brand-blue); font-weight: 700; }

  .link-list { position: absolute; left: 396px; top: 257px; font-size: 9.5px; color: var(--brand-blue); }
  .link-list li { height: 18px; display: flex; align-items: center; gap: 7px; }
  .link-list svg { width: 6px; height: 8px; }

  .site-footer { position: absolute; left: 0; top: 506px; width: 1200px; height: 242px; background: var(--footer-bg); border-top: 4px solid var(--brand-blue); color: var(--footer-muted); font-size: 9.5px; }
  .footer-brand { position: absolute; left: 162px; top: 44px; display: flex; align-items: center; gap: 12px; font-size: 20px; font-weight: 600; color: var(--white); }
  .footer-brand .brand-mark { background: var(--white); }
  .footer-about { position: absolute; left: 162px; top: 89px; width: 205px; font-size: 8.5px; line-height: 13.5px; color: #e0e0e0; }
  .footer-col h3 { position: absolute; font-size: 12px; font-weight: 700; color: var(--footer-heading); }
  .footer-nav { position: absolute; left: 461px; top: 61px; }
  .footer-nav li { height: 18px; }
  .footer-nav li.current { color: var(--white); }
  .hours-table, .contact-table { position: absolute; border-collapse: collapse; font-size: 9.5px; }
  .hours-table { left: 611px; top: 60px; }
  .hours-table td { height: 18px; padding: 0; }
  .hours-table td:first-child { width: 91px; }
  .contact-table { left: 838px; top: 60px; }
  .contact-table td { padding: 0; vertical-align: top; line-height: 15px; }
  .contact-table td:first-child { width: 89px; }

  .footer-bottom { position: absolute; left: 0; top: 203px; width: 1200px; height: 35px; border-top: 1px solid var(--footer-rule); font-size: 9.5px; }
  .footer-bottom .copyright { position: absolute; left: 162px; top: 10px; }
  .footer-bottom .legal-links a { position: absolute; top: 10px; }
</style>
</head>
<body>
  <div class="top-bar">
    <div class="contact-line">To help Here : 250 640 1187<span class="sep"></span>Email : hello@larchwell.ca</div>
    <div class="quick-links"><a href="#">Book an Appointment</a><span class="sep"></span><a href="#">Physician Toolbox</a></div>
  </div>

  <header class="site-header">
    <a class="brand" href="#"><span class="brand-mark"></span>Larchwell Clinic</a>
    <nav class="main-nav">
      <a href="#" style="left:571px">Home</a>
      <a href="#" style="left:639px">Our Clinic</a>
      <a href="#" style="left:726px">Our Staff</a>
      <a href="#" class="active" style="left:803px">Resources</a>
      <a href="#" style="left:897px">Alerts</a>
      <a href="#" style="left:964px">Contact Us</a>
    </nav>
  </header>

  <section class="page-title-band">
    <h1>RESOURCES LINKS</h1>
    <p class="breadcrumb">HOME / RESOURCES/LINKS</p>
  </section>

  <h2 class="section-heading side-nav-heading">RESOURCES LINKS</h2>
  <ul class="side-nav">
    <li class="current"><a href="#">Local Services</a></li>
    <li><a href="#">RDV and Drug Coverage</a></li>
    <li><a href="#">Mental Health Resources</a></li>
  </ul>

  <h2 class="section-heading content-heading">LOCAL SERVICES</h2>
  <ul class="link-list">
    <li><svg viewBox="0 0 6 8"><path d="M1 1l3 3-3 3" fill="none" stroke="#333" stroke-width="1.3"/></svg><a href="#">Lorem Ipsum is simply dummy text of the printing.</a></li>
    <li><svg viewBox="0 0 6 8"><path d="M1 1l3 3-3 3" fill="none" stroke="#333" stroke-width="1.3"/></svg><a href="#">Typesetting industryhas been the industry's standard.</a></li>
    <li><svg viewBox="0 0 6 8"><path d="M1 1l3 3-3 3" fill="none" stroke="#333" stroke-width="1.3"/></svg><a href="#">Dummy text ever since the 1500s, when an unknown printer.</a></li>
    <li><svg viewBox="0 0 6 8"><path d="M1 1l3 3-3 3" fill="none" stroke="#333" stroke-width="1.3"/></svg><a href="#">Took a galley of type and scrambled it to make a type specimen book.</a></li>
    <li><svg viewBox="0 0 6 8"><path d="M1 1l3 3-3 3" fill="none" stroke="#333" stroke-width="1.3"/></svg><a href="#">It has survived not only five centuries, but also the leap into electronic typesetting.</a></li>
    <li><svg viewBox="0 0 6 8"><path d="M1 1l3 3-3 3" fill="none" stroke="#333" stroke-width="1.3"/></svg><a href="#">Remaining essentially unchanged.</a></li>
    <li><svg viewBox="0 0 6 8"><path d="M1 1l3 3-3 3" fill="none" stroke="#333" stroke-width="1.3"/></svg><a href="#">Lorem Ipsum is simply dummy text of the printing.</a></li>
    <li><svg viewBox="0 0 6 8"><path d="M1 1l3 3-3 3" fill="none" stroke="#333" stroke-width="1.3"/></svg><a href="#">Typesetting industryhas been the industry's standard.</a></li>
    <li><svg viewBox="0 0 6 8"><path d="M1 1l3 3-3 3" fill="none" stroke="#333" stroke-width="1.3"/></svg><a href="#">Dummy text ever since the 1500s, when an unknown printer.</a></li>
    <li><svg viewBox="0 0 6 8"><path d="M1 1l3 3-3 3" fill="none" stroke="#333" stroke-width="1.3"/></svg><a href="#">Took a galley of type and scrambled it to make a type specimen book.</a></li>
  </ul>

  <footer class="site-footer">
    <div class="footer-brand"><span class="brand-mark"></span>Larchwell Clinic</div>
    <p class="footer-about">Lorem Ipsum is simply dummy text of the printing and typesetting industry. Lorem Ipsum has been the industry's standard dummy text</p>

    <div class="footer-col">
      <h3 style="left:461px;top:37px">Navigation</h3>
      <ul class="footer-nav">
        <li class="current"><a href="#">Home</a></li>
        <li><a href="#">Our Clinic</a></li>
        <li><a href="#">Newsletter</a></li>
        <li><a href="#">Our Staff</a></li>
        <li><a href="#">Resources</a></li>
      </ul>
    </div>

    <div class="footer-col">
      <h3 style="left:611px;top:36px">Hours of Opration</h3>
      <table class="hours-table">
        <tr><td>Monday :</td><td>8:00 AM - 6:00 PM</td></tr>
        <tr><td>Tuesday :</td><td>8:00 AM - 6:00 PM</td></tr>
        <tr><td>Wednessday :</td><td>8:00 AM - 6:00 PM</td></tr>
        <tr><td>Thursday :</td><td>8:00 AM - 6:00 PM</td></tr>
        <tr><td>Friday :</td><td>8:00 AM - 6:00 PM</td></tr>
        <tr><td>Saturday :</td><td>9:00 AM - 4:00 PM</td></tr>
        <tr><td>Sunday :</td><td>9:00 AM - 4:00 PM</td></tr>
      </table>
    </div>

    <div class="footer-col">
      <h3 style="left:836px;top:36px">Contact Us</h3>
      <table class="contact-table">
        <tr><td>Telephone :</td><td>250-640-1188</td></tr>
        <tr><td>Email:</td><td>hello@larchwell.ca</td></tr>
        <tr><td>Address:</td><td>48 Fernhill Road<br>&nbsp;Kelowna,B.C. Canada,<br>&nbsp;V1Y 2K7</td></tr>
      </table>
    </div>

    <div class="footer-bottom">
      <p class="copyright">© 2015 Larchwell Clinic. All Rights Reservsd</p>
      <nav class="legal-links">
        <a href="#" style="left:462px">About Us</a>
        <a href="#" style="left:530px">Terms of Use</a>
        <a href="#" style="left:615px">Privacy Policy</a>
      </nav>
    </div>
  </footer>
</body>
</html>
```